Fernhollow Glow Clinic is a rebranding of fernhollowfootcare.com.au. The business provides Medical Injectables (botox and fillers) Laser and IPL therapies, Podiatry and remedial massage. We have a logo already done (yay! sketch hive!) you can download it here: http://fernhollowglowclinic.com/brand_assets.zip . We are after a clean, long scrolling website (in the style of quvaret.com). There will be 6 subpages (or sections depending on how you create it) (1) Cosmetic Injections (2) Podiatry (3) Remedial Massage (4) Laser Therapies (5) Skin Care (6) Customer Club and Special Offers. The target demographic is wealthy or aspirational women 35+.

Font styles to use
Sans Serif

Colors
9bcb3c
33a6d7

Requirements
Must have
• Simple, clean long scroller like quvaret.com
Nice to have
• Congruence with existing corporate identity.

```html
<!DOCTYPE html>
<html lang="en">
<head>
<meta charset="utf-8">
<title>Fernhollow Glow Clinic</title>
<link rel="stylesheet" href="https://fonts.googleapis.com/css2?family=Roboto:ital,wght@0,300;0,400;0,500;1,300;1,400&display=swap">
<style>
:root{
  --green:#9bcb3c;
  --green-dark:#7fb33a;
  --blue:#33a6d7;
  --blue-deep:#1f8fd3;
  --text:#555a5e;
  --band-green:#cfe7b3;
  --band-blue:#c2e4ef;
  --white:#ffffff;
  --rule:#d8dcdf;
}
*{box-sizing:border-box;margin:0;padding:0}
html,body{width:1200px;height:3516px;overflow:hidden}
body{font-family:"Roboto",sans-serif;color:var(--text);background:var(--white);position:relative}
.wrap{width:938px;margin:0 auto;position:relative;height:100%}

/* header */
.site-header{height:113px}
.brand{position:absolute;left:0;top:34px;display:flex;align-items:center;gap:12px}
.brand-dot{width:26px;height:26px;border-radius:50%;background:var(--green)}
.brand-name{font-size:27px;font-weight:300;color:var(--blue);letter-spacing:.5px}
.header-phone{position:absolute;right:0;top:34px;display:flex;gap:12px;align-items:flex-start}
.header-phone .num{font-size:22px;font-weight:500;color:var(--blue);line-height:24px}
.header-phone .sub{font-size:12px;color:#333;line-height:15px}

/* nav */
.main-nav{height:47px;background:linear-gradient(90deg,#8fcb6b,#6fa86a)}
.main-nav ul{list-style:none;display:flex;height:47px;align-items:center}
.main-nav li{font-size:14px;color:var(--white);padding:0 28px;height:47px;line-height:47px;position:relative}
.main-nav li+li::before{content:"";position:absolute;left:0;top:17px;height:13px;border-left:1px solid rgba(255,255,255,.5)}
.main-nav li.active{background:var(--blue);padding:0 22px}
.main-nav li.active+li::before{display:none}

/* hero */
.hero{height:520px;background:linear-gradient(90deg,#d9eef6 0%,#6fbbe0 45%,#1c74c4 100%);position:relative}
.hero-photo{position:absolute;left:0;top:0;width:640px;height:520px;background:linear-gradient(90deg,#c9b7a8 0%,#b9d7e6 60%,rgba(111,187,224,0) 100%)}
.hero-copy{position:absolute;left:661px;top:175px;width:420px;color:var(--white)}
.hero-copy h1{font-weight:300;font-size:50px;line-height:56px}
.hero-copy p{font-size:17px;line-height:26px;margin-top:6px}
.btn-solid{display:inline-block;margin-top:14px;background:var(--green);color:var(--white);font-size:15px;padding:8px 16px}

/* welcome */
.welcome{height:260px;text-align:center}
.welcome h2{padding-top:52px;font-weight:300;font-size:33px;color:var(--blue);display:inline-block;border-bottom:1px solid var(--rule);padding-bottom:8px;padding-left:10px;padding-right:10px}
.welcome h2 span{color:var(--blue)}
.welcome p{font-size:14px;line-height:24px;margin-top:20px;text-align:left}

/* service bands */
.service{height:422px;position:relative;overflow:hidden}
.service.tint-green{background:var(--band-green)}
.service.tint-blue{background:var(--band-blue)}
.service.tint-white{background:var(--white)}
.service-photo{position:absolute;top:0;height:422px;width:700px}
.service-photo.left{left:0}
.service-photo.right{right:0}
.service-copy{position:absolute;top:80px;width:516px}
.service-copy.right{left:553px}
.service-copy.left{left:131px}
.service-copy h3{font-weight:300;font-size:33px;line-height:40px}
.service-copy.blue h3{color:var(--blue)}
.service-copy.green h3{color:var(--green)}
.service-copy p{font-size:14.5px;line-height:24px;margin-top:8px}
.btn-line{display:inline-block;margin-top:16px;font-size:13px;padding:6px 9px;border:1px solid currentColor;background:rgba(255,255,255,.5)}
.service-copy.blue .btn-line{color:var(--blue)}
.service-copy.green .btn-line{color:var(--green)}

/* testimonials */
.testimonials{height:286px;text-align:center;position:relative}
.testimonials h2{padding-top:40px;font-weight:300;font-size:31px;color:var(--green);display:inline-block;border-bottom:1px solid var(--rule);padding-bottom:8px;padding-left:36px;padding-right:36px}
.quote-person{position:absolute;left:141px;top:120px;width:105px;text-align:center}
.avatar{width:105px;height:105px;border-radius:50%;background:linear-gradient(180deg,#cfa89a,#f0e3dc)}
.quote-person .name{font-size:14px;color:var(--green);margin-top:10px}
.quote-text{position:absolute;left:274px;top:124px;width:795px;text-align:left;font-style:italic;font-size:14px;line-height:24px;color:#666}
.quote-text .mark{font-size:34px;color:#ccc;position:absolute;left:-2px;top:-12px;font-style:normal}
.quote-text p{text-indent:26px}
.slider-arrows{position:absolute;right:131px;top:268px;display:flex;gap:8px}

/* footer */
.site-footer{height:182px;background:var(--blue-deep);color:var(--white);position:relative}
.footer-col{position:absolute;top:36px}
.footer-col h4{font-weight:400;font-size:18px;margin-bottom:14px}
.mailing{left:131px;width:320px}
.fields{display:flex;gap:14px}
.field{width:152px;height:26px;background:var(--white);color:#333;font-size:12px;padding:5px 8px;font-style:italic}
.btn-submit{margin-top:12px;display:inline-block;border:1px solid var(--white);font-size:13px;padding:5px 14px}
.contact{left:480px;width:400px}
.contact-row{display:flex;gap:10px;font-size:12px;line-height:15px;align-items:flex-start}
.contact-grid{display:flex;gap:24px}
.contact-grid .stack div+div{margin-top:10px}
.social{right:131px;text-align:right;top:50px}
.social .circles{display:flex;gap:8px;justify-content:flex-end}
.social .circles span{width:26px;height:26px;border-radius:50%;border:1.5px solid var(--white)}
.social p{font-size:12px;line-height:16px;margin-top:8px}
</style>
</head>
<body>

<header class="site-header">
  <div class="wrap">
    <div class="brand"><span class="brand-dot"></span><span class="brand-name">Fernhollow Glow Clinic</span></div>
    <div class="header-phone">
      <svg width="38" height="40" viewBox="0 0 38 40"><circle cx="19" cy="19" r="16" fill="none" stroke="#33a6d7" stroke-width="3"/><path d="M13 12c1-1 3-1 3 1l1 3c0 1-1 2-1 2 1 2 3 4 5 5 0 0 1-1 2-1l3 1c2 0 2 2 1 3-2 2-5 2-9-1s-6-7-5-13z" fill="#33a6d7"/><path d="M19 35l-4 5h8z" fill="#33a6d7"/></svg>
      <div><div class="num">123-456-7890</div><div class="sub">Lorem ipsum dolor sit amet,<br>consectetuer adipiscing elit</div></div>
    </div>
  </div>
</header>

<nav class="main-nav">
  <div class="wrap">
    <ul>
      <li class="active">Home</li><li>About Us</li><li>Services</li><li>Specials/Packages</li><li>Gift Vouchers</li><li>Product Range</li><li>Contact Us</li>
    </ul>
  </div>
</nav>

<section class="hero">
  <div class="hero-photo" role="img" aria-label="Portrait photo of a woman with smooth skin touching her face"></div>
  <div class="hero-copy">
    <h1>Skin Rejuvenation</h1>
    <p>Lorem ipsum dolor sit amet, consectetuer adipiscing elit, sed diam nonummy nibh euismod tincidunt ut laoreet dolore magna aliquam erat volutpat.</p>
    <span class="btn-solid">More Detail</span>
  </div>
</section>

<section class="welcome">
  <div class="wrap">
    <h2>Welcome To <span>Fernhollow Glow Clinic</span></h2>
    <p>Lorem ipsum dolor sit amet, consectetuer adipiscing elit, sed diam nonummy nibh euismod tincidunt ut laoreet dolore magna aliquam erat volutpat. Ut wisi enim ad minim veniam, quis nostrud exerci tation ullamcorper suscipit lobortis nisl ut aliquip ex ea commodo consequat. Duis autem vel eum iriure dolor in hendrerit in vulputate velit esse molestie consequat, vel illum dolore eu feugiat nulla facilisis at vero eros et accumsan et iusto odio dignissim qui blandit praesent luptatum zzril delenit augue duis dolore te feugait nulla facilisi.</p>
  </div>
</section>

<section class="service tint-green">
  <div class="service-photo left" role="img" aria-label="Photo of a cosmetic injection being given to a client" style="background:linear-gradient(90deg,#d8cbb8 0%,#d9dcc0 55%,rgba(207,231,179,0) 100%)"></div>
  <div class="service-copy right blue">
    <h3>Cosmetic Injections</h3>
    <p>Lorem ipsum dolor sit amet, consectetuer adipiscing elit, sed diam nonummy nibh euismod tincidunt ut laoreet dolore magna aliquam erat volutpat. Ut wisi enim ad minim veniam, quis nostrud exerci tation ullamcorper suscipit lobortis nisl ut aliquip ex ea commodo consequat. Duis autem vel eum iriure dolor in hendrerit in vulputate velit esse molestie consequat, vel illum dolore eu feugiat nulla facilisis at vero eros et accumsan et iusto odio dignissim qui blandit praesent luptatum zzril delenit augue duis dolore te feugait nulla facilisi.</p>
    <span class="btn-line">Read More</span>
  </div>
</section>

<section class="service tint-white">
  <div class="service-photo right" role="img" aria-label="Photo of hands caring for a foot" style="background:linear-gradient(270deg,#eee2dc 0%,#f3ece8 50%,rgba(255,255,255,0) 100%)"></div>
  <div class="service-copy left green">
    <h3>Podiatry</h3>
    <p>Lorem ipsum dolor sit amet, consectetuer adipiscing elit, sed diam nonummy nibh euismod tincidunt ut laoreet dolore magna aliquam erat volutpat. Ut wisi enim ad minim veniam, quis nostrud exerci tation ullamcorper suscipit lobortis nisl ut aliquip ex ea commodo consequat. Duis autem vel eum iriure dolor in hendrerit in vulputate velit esse molestie consequat, vel illum dolore eu feugiat nulla facilisis at vero eros et accumsan et iusto odio dignissim qui blandit praesent luptatum zzril delenit augue duis dolore te feugait nulla facilisi.</p>
    <span class="btn-line">Read More</span>
  </div>
</section>

<section class="service tint-blue">
  <div class="service-photo left" role="img" aria-label="Photo of a woman receiving a back massage" style="background:linear-gradient(90deg,#cdb3a0 0%,#c9d2cf 55%,rgba(194,228,239,0) 100%)"></div>
  <div class="service-copy right blue">
    <h3>Remedial Massage</h3>
    <p>Lorem ipsum dolor sit amet, consectetuer adipiscing elit, sed diam nonummy nibh euismod tincidunt ut laoreet dolore magna aliquam erat volutpat. Ut wisi enim ad minim veniam, quis nostrud exerci tation ullamcorper suscipit lobortis nisl ut aliquip ex ea commodo consequat. Duis autem vel eum iriure dolor in hendrerit in vulputate velit esse molestie consequat, vel illum dolore eu feugiat nulla facilisis at vero eros et accumsan et iusto odio dignissim qui blandit praesent luptatum zzril delenit augue duis dolore te feugait nulla facilisi.</p>
    <span class="btn-line">Read More</span>
  </div>
</section>

<section class="service tint-white">
  <div class="service-photo right" role="img" aria-label="Photo of a woman reclining during a laser treatment" style="background:linear-gradient(270deg,#e4ddd8 0%,#ece7e3 50%,rgba(255,255,255,0) 100%)"></div>
  <div class="service-copy left green">
    <h3>Laser Therapies</h3>
    <p>Lorem ipsum dolor sit amet, consectetuer adipiscing elit, sed diam nonummy nibh euismod tincidunt ut laoreet dolore magna aliquam erat volutpat. Ut wisi enim ad minim veniam, quis nostrud exerci tation ullamcorper suscipit lobortis nisl ut aliquip ex ea commodo consequat. Duis autem vel eum iriure dolor in hendrerit in vulputate velit esse molestie consequat, vel illum dolore eu feugiat nulla facilisis at vero eros et accumsan et iusto odio dignissim qui blandit praesent luptatum zzril delenit augue duis dolore te feugait nulla facilisi.</p>
    <span class="btn-line">Read More</span>
  </div>
</section>

<section class="service tint-green">
  <div class="service-photo left" role="img" aria-label="Close-up portrait photo of a woman with glowing skin" style="background:linear-gradient(90deg,#6d5a4c 0%,#c7ae98 40%,rgba(207,231,179,0) 100%)"></div>
  <div class="service-copy right blue">
    <h3>Skin Care</h3>
    <p>Lorem ipsum dolor sit amet, consectetuer adipiscing elit, sed diam nonummy nibh euismod tincidunt ut laoreet dolore magna aliquam erat volutpat. Ut wisi enim ad minim veniam, quis nostrud exerci tation ullamcorper suscipit lobortis nisl ut aliquip ex ea commodo consequat. Duis autem vel eum iriure dolor in hendrerit in vulputate velit esse molestie consequat, vel illum dolore eu feugiat nulla facilisis at vero eros et accumsan et iusto odio dignissim qui blandit praesent luptatum zzril delenit augue duis dolore te feugait nulla facilisi.</p>
    <span class="btn-line">Read More</span>
  </div>
</section>

<section class="testimonials">
  <h2>Client Testimonials</h2>
  <div class="quote-person">
    <div class="avatar" role="img" aria-label="Client portrait photo"></div>
    <div class="name">Mara Ellison</div>
  </div>
  <div class="quote-text">
    <span class="mark">&ldquo;</span>
    <p>Lorem ipsum dolor sit amet, consectio mol adipiscing elit, sed dia nonumiy nibh sitamant consecti uerol adipiscing elit, sedil dial nonuolu my nibh euismod. Lorem ipsum dolor sit amet, consectio mol adipiscing elit, sed dia nonumiy nibh sitamant cons ecti uerol adipiscing elit, sed dial nonuolu my nibh euismod. Lorem ipsum dolor sit amet, consectio mol adipiscing elit, sed dian nonumiy nibh sitamant cons e nibh euismod.</p>
  </div>
  <div class="slider-arrows">
    <svg width="18" height="18" viewBox="0 0 18 18"><circle cx="9" cy="9" r="8" fill="none" stroke="#9bcb3c" stroke-width="1.5"/><path d="M10.5 5.5L7 9l3.5 3.5" fill="none" stroke="#9bcb3c" stroke-width="1.5"/></svg>
    <svg width="18" height="18" viewBox="0 0 18 18"><circle cx="9" cy="9" r="8" fill="none" stroke="#9bcb3c" stroke-width="1.5"/><path d="M7.5 5.5L11 9l-3.5 3.5" fill="none" stroke="#9bcb3c" stroke-width="1.5"/></svg>
  </div>
</section>

<footer class="site-footer">
  <div class="footer-col mailing">
    <h4>Join The Mailing List</h4>
    <div class="fields"><div class="field">Name</div><div class="field">Email</div></div>
    <span class="btn-submit">Submit</span>
  </div>
  <div class="footer-col contact">
    <h4>Contact Information</h4>
    <div class="contact-grid">
      <div class="contact-row">
        <svg width="14" height="20" viewBox="0 0 14 20"><path d="M7 0a7 7 0 0 0-7 7c0 5 7 13 7 13s7-8 7-13a7 7 0 0 0-7-7zm0 10a3 3 0 1 1 0-6 3 3 0 0 1 0 6z" fill="#fff"/></svg>
        <div>Lorem ipsum dolor sit ame<br>consectetuer ina adipiscing<br>consectetuer ina</div>
      </div>
      <div class="stack">
        <div class="contact-row"><svg width="14" height="14" viewBox="0 0 14 14"><path d="M3 1c1-1 2 0 2 1l1 2c0 1-1 1-1 2 1 2 2 3 3 3 1 0 1-1 2-1l2 1c1 0 2 1 1 2-2 2-4 2-7-1S1 3 3 1z" fill="#fff"/></svg><span style="font-weight:500">0123-456-789</span></div>
        <div class="contact-row"><svg width="14" height="12" viewBox="0 0 14 12"><rect x="0.5" y="0.5" width="13" height="11" fill="none" stroke="#fff"/><path d="M1 1l6 5 6-5" fill="none" stroke="#fff"/></svg><span>info@yoursitename.com</span></div>
      </div>
    </div>
  </div>
  <div class="footer-col social">
    <div class="circles"><span></span><span></span><span></span><span></span></div>
    <p>&copy; 2014 Fernhollow Glow Clinic.<br>All Rights Reserved.</p>
  </div>
</footer>

</body>
</html>
```